Business Card Design for Fashion Tech Startup

Dear designers, we need a business card for Asia's premier fashion tech startup.!

PebbleHop is discovery e-commerce destination for busy, discerning parents in Asia featuring leading independent designers of baby, kids fashion apparel and sustainable brands from around the world.

PebbleHop is a modern, contemporary fashion tech startup targeting well-educated, well travelled and affluent parents. We're NOT your typical kiddy store!! Our design philosophy & e-commerce site is more like Vask.com, Orimesa.com, Pondwick.com, Farthollow.com.
Updates

Hi, size of the business card should be 84mm X 55mm. Would appreciate some business card layouts in Portrait as added consideration, i fancy the idea of a Portrait business card. What's important is that the business card should pique the receiver's interest to log onto the website to learn more. Many thanks and love forward to the designs!

Target Market(s)

Though modern, classy in look, feel & positioning, PebbleHop does possess a cheeky, fun-loving personality as depicted by its logo and the segment it targets (baby, kids) though the key decision makers i.e primarily mums between 25-40 who are well educated/travelled, local & expatriates, internet/digitally savvy, mid-high income working mums.

Industry/Entity Type

E-Commerce

Requirements
Must have
• Name, designation, email, phone & mobile number.
Company url : www.pebblehop.sg
Slogan : Discovery e-commerce destination for discerning, busy parents
Nice to have
• Call to Action such as a Discount code offering 10% discount
or asking people to "Like" us on our Chatterly page/Chatterly URL

```html
<!DOCTYPE html>
<html lang="en">
<head>
<meta charset="utf-8">
<title>PebbleHop Business Card</title>
<link href="https://fonts.googleapis.com/css2?family=Roboto:wght@300;400;700&display=swap" rel="stylesheet">
<style>
  :root {
    --backdrop: #e9e7e3;
    --paper: #f3f2ed;
    --paper-grey: #dfe3e3;
    --band-grey: #e4e7e7;
    --navy: #2d4b63;
    --navy-band: #3a5a70;
    --coral: #f0735c;
    --coral-panel: #f27a66;
    --slogan: #c9d2d8;
    --ink-soft: #4c6275;
  }
  * { box-sizing: border-box; margin: 0; padding: 0; }
  html, body {
    width: 1200px; height: 1000px; overflow: hidden;
    background: var(--backdrop);
    font-family: "Roboto", Arial, sans-serif;
  }
  .stage {
    width: 1200px; height: 1000px;
    display: flex; justify-content: center; align-items: center; gap: 80px;
  }
  .card {
    width: 380px; height: 580px;
    background: var(--paper);
    box-shadow: 0 6px 18px rgba(0,0,0,0.15);
    display: flex; flex-direction: column;
    overflow: hidden;
  }
  /* Front */
  .front__brand {
    height: 250px; background: var(--paper-grey);
    display: flex; flex-direction: column; align-items: center; justify-content: center; gap: 14px;
  }
  .front__emblem { width: 150px; height: 150px; }
  .brand-name {
    font-weight: 700; color: var(--coral); font-size: 26px; letter-spacing: 0.5px;
  }
  .front__details {
    flex: 1; display: flex; flex-direction: column; align-items: center;
    padding-top: 28px; color: var(--navy); text-align: center;
  }
  .person-name { font-size: 22px; font-weight: 400; letter-spacing: 1px; }
  .person-role { font-size: 19px; color: var(--coral); margin-top: 4px; }
  .contacts { margin-top: 38px; font-weight: 300; line-height: 1.35; color: var(--ink-soft); }
  .contacts .phone { font-size: 18px; }
  .contacts .email { font-size: 21px; }
  .divider { width: 200px; height: 2px; background: var(--navy); margin-top: 62px; }
  .website { margin-top: 14px; font-size: 17px; font-weight: 300; color: var(--ink-soft); }
  /* Back */
  .back__brand {
    height: 140px; display: flex; align-items: center; justify-content: center; gap: 14px;
  }
  .back__brand .dot { width: 38px; height: 38px; border-radius: 50%; background: var(--navy); }
  .back__spacer { height: 36px; background: var(--band-grey); }
  .back__slogan {
    height: 118px; background: var(--navy-band); color: var(--slogan);
    display: flex; align-items: center; justify-content: center; text-align: center;
    font-size: 17px; font-weight: 300; line-height: 1.25; padding: 0 50px;
  }
  .back__cta {
    flex: 1; background: var(--coral-panel);
    display: flex; align-items: flex-end; justify-content: center;
    padding-bottom: 22px; color: #fbd9d1; font-size: 15px; font-weight: 300;
  }
</style>
</head>
<body>
<main class="stage">
  <section class="card card--front">
    <div class="front__brand">
      <svg class="front__emblem" viewBox="0 0 150 150" role="img" aria-label="Circular cluster of playful baby and kids items around the brand emblem">
        <circle cx="75" cy="75" r="72" fill="#e99a86"/>
      </svg>
      <span class="brand-name">PebbleHop.sg</span>
    </div>
    <div class="front__details">
      <h1 class="person-name">JOHN DOE</h1>
      <p class="person-role">CEO</p>
      <div class="contacts">
        <p class="phone">222-2222</p>
        <p class="phone">555-555-5555</p>
        <p class="email">johndoe@pebblehop.com</p>
      </div>
      <div class="divider"></div>
      <p class="website">http://www.pebblehop.sg/</p>
    </div>
  </section>

  <section class="card card--back">
    <div class="back__brand">
      <span class="dot"></span>
      <span class="brand-name">PebbleHop</span>
    </div>
    <div class="back__spacer"></div>
    <p class="back__slogan">Discovery e-commerce destination for discerning, busy parents</p>
    <p class="back__cta">Like us on Chatterly</p>
  </section>
</main>
</body>
</html>
```